Professional, Attractive, Simple Website Needed!!

We completed the design for our logo.

We need a website built out around this.

Here are a couple samples of how we want ours formatted.

http://brvntapower.com

http://www.halvorbeam.com/lp/free-quote?LeadSource=Search%20Engine&ProgramName=webquery&experience=qual&language=en&type=brd&gclid=Xq7RTPwmEYKDLAvUHbsNQkfPZrTcGwnJuoVbXeLqHmRYdAsWtPkMcNfBYgzTrUoQJhEdWvKpYaLsZbCmNDgQwTxAoKpXbT_qkR

http://morvalo.co

Reason: Extending this deadline due to our delay in providing designers with content for each page. This is coming in next 24 hours.

Reason: Due to scheduling conflicts and extended travel delays related to Puerto Rico, the deadline has been extended. Your patience is greatly appreciated.

Reason: Travel and scheduling conflicts have made it impossible to give this project the thorough review it deserves, therefore I am extending the deadline. Thank you for your patience!

Target Market(s)

Home Owners who earn 60k + household annually

Industry/Entity Type

It Professional

Coding

Coded - Design and coding required

Number of Pages Required

5+ page

Font styles to use
Serif

Colors
34a7d8
9bcb3c

Requirements
Must have
• Simple
• Lead form Entry (Ability for visitor to enter Name, number and address for a quote)
• Sleek Design
• Professional
• Testimonials
• Use color Scheme of Design Logo Attached
Nice to have
• Video when site starts
• Like this
• https://www.vidmarrow.com/watch?v=qT8mRpXw2Ka&feature=vidm.ro
Should not have
• Should not include Commercial solar
• Should not include wind power

```html
<!DOCTYPE html>
<html lang="en">
<head>
<meta charset="utf-8">
<title>About Solvane Energy</title>
<link rel="stylesheet" href="https://fonts.googleapis.com/css2?family=Roboto:wght@300;400;500&display=swap">
<style>
:root{
  --blue:#34a7d8;
  --green:#9bcb3c;
  --ink:#1c1c1c;
  --white:#ffffff;
  --hero-top:#3a5273;
  --hero-bottom:#4a4f57;
  --footer-dark:#262b33;
  --footer-mid:#3a4049;
  --bar:#1e2126;
}
*{box-sizing:border-box;margin:0;padding:0}
html,body{width:1200px;height:1185px;overflow:hidden;background:var(--white)}
body{position:relative;font-family:"Roboto",Arial,sans-serif;color:var(--ink)}
.hero{position:absolute;left:0;top:0;width:1200px;height:312px}
.hero-photo{position:absolute;inset:0;background:linear-gradient(180deg,var(--hero-top) 0%,#344866 35%,var(--hero-bottom) 100%)}
.nav-rule{position:absolute;left:0;top:69px;width:1200px;height:1px;background:rgba(255,255,255,.85)}
.nav{position:absolute;top:54px;left:0;width:1200px;font-size:9px;letter-spacing:.2px;color:var(--white);text-transform:uppercase}
.nav a{position:absolute;color:inherit;text-decoration:none;transform:translateX(-50%)}
.brand{position:absolute;left:600px;transform:translateX(-50%);display:flex;align-items:center;gap:5px;white-space:nowrap;font-weight:500;color:var(--green)}
.brand-dot{width:16px;height:16px;border:2px solid var(--blue);border-radius:50%}
.brand.top{top:28px;font-size:13px}
.hero-title{position:absolute;top:130px;width:1200px;text-align:center;color:var(--white);font-size:23px;font-weight:400}
.hero-text{position:absolute;top:161px;left:370px;width:460px;text-align:center;color:var(--white);font-size:11.4px;line-height:13.2px;font-weight:300}
.why-title{position:absolute;top:339px;width:1200px;text-align:center;font-size:23px;font-weight:400;color:#111}
.why-photo{position:absolute;left:366px;top:392px;width:468px;height:293px;background:linear-gradient(180deg,#9fb6cc 0%,#7d8ea3 22%,#5e6d85 55%,#8d939a 100%)}
.why-copy{position:absolute;top:697px;left:300px;width:600px;text-align:center;font-size:11.6px;line-height:17px;font-weight:400;color:#222}
.why-copy p+p{margin-top:17px}
.footer-shape{position:absolute;left:0;top:930px;width:1200px;height:255px}
.footer .brand{top:980px;font-size:13px}
.contact{position:absolute;left:426px;top:1041px;font-size:11.5px;color:var(--white);font-weight:400}
.contact li{list-style:none;display:flex;gap:6px;align-items:flex-start;margin-bottom:8px;line-height:17px}
.contact svg{flex:none;margin-top:2px}
.follow{position:absolute;left:700px;top:1061px;width:82px;text-align:center;color:var(--white);font-size:11px}
.social{display:flex;justify-content:center;gap:10px;margin-top:10px}
.social span{width:16px;height:16px;border:1.4px solid var(--white);border-radius:50%}
.copyright{position:absolute;left:0;top:1153px;width:1200px;height:32px;background:var(--bar);color:var(--white);font-size:7.5px;text-align:center;line-height:32px}
</style>
</head>
<body>
<header class="hero">
  <div class="hero-photo" role="img" aria-label="Upward view of a tall glass office tower against a blue sky"></div>
  <div class="nav-rule"></div>
  <div class="brand top"><span class="brand-dot"></span>Solvane Energy</div>
  <nav class="nav">
    <a href="#" style="left:361px">Home</a>
    <a href="#" style="left:432px">About us</a>
    <a href="#" style="left:510px">Services</a>
    <a href="#" style="left:689px">Gallery</a>
    <a href="#" style="left:754px">FAQ</a>
    <a href="#" style="left:827px">Contact us</a>
  </nav>
  <h1 class="hero-title">ABOUT SOLVANE ENERGY</h1>
  <p class="hero-text">Solvane Energy - is a large interregional company engaged in the sale of solar cells and modules designed to create autonomous power supply systems, as well as installation of solar stations for your home.</p>
</header>

<main>
  <h2 class="why-title">WHY WE ARE</h2>
  <div class="why-photo" role="img" aria-label="Aerial view of a residential neighbourhood with solar panels on the house roofs"></div>
  <div class="why-copy">
    <p>We offer ready-made solutions for solar systems connected to mains and standalone, projects to the engineering and technical department and our large medium and large scale: home and industrial installations on the roof and ground. Solvane Energy is an opportunity to provide ready-made solutions for all your requirements.</p>
    <p>Solvane Energy represents already developed projects for more than 170 MW; in a 700MW portfolio around the world and 300MW projects offered for distribution. Also, we are energy producers.</p>
    <p>Today, we offer NEW energy solutions. We must change the habitual practice of obtaining energy: you can receive it in a completely different way: more decentralized.</p>
    <p>It's no secret that the electricity continues to go up. And we can provide NEW EFFECTIVE AND INNOVATIVE<br>SOLUTIONS of a direct energy network in order to save your money.</p>
  </div>
</main>

<footer class="footer">
  <svg class="footer-shape" viewBox="0 0 1200 255" role="img" aria-label="Close-up of dark solar panel surface">
    <defs>
      <linearGradient id="panel" x1="0" y1="0" x2="0" y2="1">
        <stop offset="0" stop-color="#3a4049"/>
        <stop offset="0.5" stop-color="#2c323b"/>
        <stop offset="1" stop-color="#22262d"/>
      </linearGradient>
    </defs>
    <polygon points="0,93 600,0 1200,93 1200,255 0,255" fill="url(#panel)"/>
  </svg>
  <div class="brand"><span class="brand-dot"></span>Solvane Energy</div>
  <ul class="contact">
    <li><svg width="12" height="14" viewBox="0 0 12 14"><path d="M6 13s-5-5-5-8a5 5 0 0 1 10 0c0 3-5 8-5 8z" fill="none" stroke="#fff" stroke-width="1.2"/><circle cx="6" cy="5" r="1.8" fill="none" stroke="#fff" stroke-width="1.2"/></svg>Norvale, Westland</li>
    <li><svg width="14" height="11" viewBox="0 0 14 11"><rect x="0.6" y="0.6" width="12.8" height="9.8" fill="none" stroke="#fff" stroke-width="1.2"/><path d="M1 1l6 5 6-5" fill="none" stroke="#fff" stroke-width="1.2"/></svg>hello@solvane-mail.com</li>
    <li><svg width="14" height="14" viewBox="0 0 14 14"><path d="M3 1l2 3-1.5 1.5a8 8 0 0 0 5 5L10 9l3 2-1.5 2.5C6 13 1 8 .8 2.5z" fill="none" stroke="#fff" stroke-width="1.1"/></svg><span>+00(000)555-01-75<br>+00(000)555-01-76</span></li>
  </ul>
  <div class="follow">FOLLOW US
    <div class="social" aria-label="Social links"><span></span><span></span><span></span></div>
  </div>
  <div class="copyright">© 2017 Solvane Energy. All Rights Reserved</div>
</footer>
</body>
</html>
```